Flyer for the Radiant Harvest Worship Day

I am looking to create a flyer for a one day prayer retreat our church is organizing.
This flyer will be posted on social media, websites and will also be printed so it can be mailed to people.
I am looking for something professional, with good use of our logo and band colors (logo colors).
I am counting on the designer's skill, creativity, art and knowledge of media communication to produce a flyer that will effectively and quickly convey the message we are trying to spread.
CONTENT OF THE FLYER:
Event title: Radiant Harvest Worship Day
Date: Tuesday July 2nd, 2019
Time: 11:00AM - 7:00PM
Belmont Hotel, 4875 Maple Ridge Road, Portland, Maine 04219 (Room: Evergreen)
Event Key words to highlight what the event is about: Prayer, Sharing the Word, Panel discussion, prophecy, Impartation.
Key phrases:
A one day prayer retreat.
Jesus Chris is Lord
Contact info:
www.tuvela.org
Phone: 207 583 2194
Email: contact@brookmeadow.org

```html
<!DOCTYPE html>
<html lang="en">
<head>
<meta charset="utf-8">
<title>Radiant Harvest Worship Day</title>
<link rel="stylesheet" href="https://fonts.googleapis.com/css2?family=Alegreya+Sans:wght@400&family=Cinzel:wght@400&family=Cormorant+Garamond:wght@500&family=Pinyon+Script&display=swap">
<style>
  :root {
    --sky-top: #3f9fc8;
    --sky-mid: #9cc6c4;
    --glow: #e9b673;
    --earth: #6a5848;
    --dusk: #24344a;
    --night: #0e2036;
    --ink: #10233a;
    --white: #ffffff;
    --accent: #f39a1e;
  }
  * { margin: 0; padding: 0; box-sizing: border-box; }
  html, body { width: 942px; height: 1200px; overflow: hidden; background: var(--night); }
  .flyer {
    position: relative;
    width: 942px;
    height: 1200px;
    overflow: hidden;
    text-align: center;
  }
  .flyer-photo {
    position: absolute;
    inset: 0;
    background:
      radial-gradient(ellipse 55% 38% at 52% 58%, rgba(196,170,140,0.55), rgba(196,170,140,0) 70%),
      linear-gradient(180deg,
        var(--sky-top) 0%,
        #62b2cf 20%,
        var(--sky-mid) 36%,
        #d9c08f 50%,
        var(--glow) 57%,
        #a98a68 68%,
        var(--earth) 76%,
        var(--dusk) 86%,
        var(--night) 100%);
  }
  .brand {
    position: absolute;
    top: 92px;
    left: 0;
    width: 100%;
    font-family: "Cormorant Garamond", serif;
    font-weight: 500;
    font-size: 92px;
    line-height: 1;
    letter-spacing: 2px;
    color: var(--white);
  }
  .tagline {
    position: absolute;
    top: 226px;
    left: 0;
    width: 100%;
    font-family: "Alegreya Sans", sans-serif;
    font-size: 20px;
    letter-spacing: 0.6px;
    color: var(--white);
  }
  .event-kicker {
    position: absolute;
    top: 323px;
    left: 0;
    width: 100%;
    font-family: "Cinzel", serif;
    font-size: 29px;
    color: var(--ink);
  }
  .event-title {
    position: absolute;
    top: 375px;
    left: 0;
    width: 100%;
    font-family: "Pinyon Script", cursive;
    font-size: 150px;
    line-height: 1.2;
    color: var(--ink);
  }
  .keywords {
    position: absolute;
    top: 938px;
    left: 0;
    width: 100%;
    font-family: "Cinzel", serif;
    font-size: 17px;
    color: var(--white);
  }
  .rule {
    position: absolute;
    left: 156px;
    width: 630px;
    height: 3px;
    background: var(--accent);
  }
  .rule--top { top: 995px; }
  .rule--bottom { top: 1085px; }
  .event-date {
    position: absolute;
    top: 1023px;
    left: 0;
    width: 100%;
    font-family: "Cormorant Garamond", serif;
    font-weight: 500;
    font-size: 33px;
    color: var(--white);
  }
  .venue {
    position: absolute;
    top: 1112px;
    left: 0;
    width: 100%;
    font-family: "Cormorant Garamond", serif;
    font-weight: 500;
    font-size: 21px;
    color: var(--white);
  }
</style>
</head>
<body>
  <main class="flyer">
    <div class="flyer-photo" role="img" aria-label="Photo of folded praying hands blended with a sunset sky and bare trees, fading into a dark blue base"></div>

    <div class="brand">Tuvela</div>
    <p class="tagline">A ONE DAY PRAYER RETREAT. JESUS CHRIS IS LORD</p>

    <p class="event-kicker">RADIANT HARVEST</p>
    <h1 class="event-title">Worship Day</h1>

    <p class="keywords">PRAYER, SHARING THE WORD, PANEL DISCUSSION, PROPHECY, IMPARTATION.</p>

    <div class="rule rule--top"></div>
    <p class="event-date">Tuesday July 2nd, 2019 11:00AM - 7:00PM</p>
    <div class="rule rule--bottom"></div>

    <p class="venue">Belmont Hotel, 4875 Maple Ridge Road, Portland, Maine 04219 (Room: Evergreen)</p>
  </main>
</body>
</html>
```